Billboard Kernhuis - Atelier Z

I need two Billboards (125cm width x 340 height) -. They will be standing side by side in front of a building. Each billboard contains details of a business. 1. Medical center: KERNHUIS MARVELDE 2. Beauty saloon/Permanent make-up. ATELIER Z & PMU Clinic. We already have a mockup. (see uploads). We want a design fitting the building with upmarket look. Modern, fresh and classy. The billboards need to have the same background color as in the mockup: dark-grey/black. The medical center has a green accent and the Beauty salon soft pink. The billboards should have certain uniformity.

Target Market(s)

Upmarket men and women

Font styles to use
Sans Serif

Requirements
Must have
• WE LIKE OUT OF THE BOX DESIGNS

KERNHUIS MARVELDE
Uw rug is onze zorg - this is the tagline
hello@kernhuismarvelde-demo.be
09 481 26 70
www.kernhuismarvelde-demo.be
facebook icon | instagram icon

ATELIER Z (HAS TWO DEPARTMENTS)
1. Schoonheidsinstituut - (which means beauty salon)
2. LINEA (which means permanent make up)
0486 51 93 40
hello@atelierz-demo.be
www.atelierz-demo.be

hello@atelierz-demo.be
Should not have
• not curly, not kitch, no color-books
NO PICTURES IN DESIGN

```html
<!DOCTYPE html>
<html lang="nl">
<head>
<meta charset="utf-8">
<title>Billboards Atelier Z en Kernhuis Marvelde</title>
<link href="https://fonts.googleapis.com/css2?family=Montserrat:wght@300;400;500&display=swap" rel="stylesheet">
<style>
  :root {
    --stage: #d6d6d6;
    --board: #3e3e40;
    --shade: #5e5e5e;
    --blush: #f5e8e7;
    --green: #84c757;
    --ink: #3d3d3f;
    --ink-soft: #4a4a4c;
    --dot: #555557;
    --white: #ffffff;
  }
  * { margin: 0; padding: 0; box-sizing: border-box; }
  html, body { width: 1200px; height: 1200px; overflow: hidden; }
  body { background: var(--stage); font-family: "Montserrat", sans-serif; position: relative; }

  .billboard { position: absolute; top: 88px; width: 382px; height: 1040px; background: var(--board); overflow: hidden; }
  .billboard--atelier { left: 229px; }
  .billboard--kernhuis { left: 659px; }
  .billboard__shapes { position: absolute; inset: 0; width: 100%; height: 100%; }

  .line { position: absolute; left: 0; width: 100%; text-align: center; white-space: nowrap; }

  /* Atelier Z */
  .brand-mark { position: absolute; left: 171px; top: 52px; width: 40px; height: 40px; border: 1.5px solid var(--white); }
  .brand-name { top: 150px; color: var(--white); font-weight: 300; font-size: 24px; letter-spacing: 22px; text-indent: 22px; }
  .brand-sub { top: 204px; color: var(--white); font-weight: 400; font-size: 7px; letter-spacing: 8.6px; text-indent: 8.6px; }
  .studio-name { top: 316px; color: var(--white); font-weight: 300; font-size: 34px; letter-spacing: 12px; text-indent: 12px; }
  .studio-by { top: 397px; color: var(--white); font-weight: 400; font-size: 10px; letter-spacing: 2.6px; text-indent: 2.6px; }

  .dept { color: var(--ink); font-weight: 400; font-size: 24px; }
  .detail { color: var(--ink); font-weight: 400; font-size: 17.5px; }
  .dept--beauty { top: 563px; }
  .detail--web1 { top: 600px; }
  .detail--book { top: 627px; }
  .dept--pmu { top: 679px; color: var(--ink-soft); }
  .detail--web2 { top: 715px; }
  .detail--advice { top: 742px; }
  .detail--phone { top: 769px; }

  .socials { position: absolute; left: 0; width: 100%; display: flex; justify-content: center; gap: 8px; }
  .socials--atelier { top: 817px; }
  .socials--kernhuis { top: 499px; }
  .social { width: 29px; height: 29px; border-radius: 50%; background: var(--dot); border: 1.5px solid var(--ink); }

  /* Kernhuis */
  .k-name { position: absolute; left: 75px; top: 164px; color: var(--white); font-weight: 500; font-size: 22px; letter-spacing: 3px; line-height: 27px; }
  .tagline { top: 352px; color: var(--ink); font-size: 24px; font-weight: 400; }
  .k-detail { color: var(--ink); font-size: 18px; font-weight: 400; letter-spacing: 0.3px; }
  .k-web { top: 398px; }
  .k-phone { top: 425px; }
  .k-mail { top: 452px; }
</style>
</head>
<body>

<section class="billboard billboard--atelier" aria-label="Billboard Atelier Z">
  <svg class="billboard__shapes" viewBox="0 0 615 1674" preserveAspectRatio="none" aria-hidden="true">
    <polygon points="0,806 171,836 0,876" fill="var(--shade)"/>
    <polygon points="441,1393 615,1349 615,1427" fill="var(--shade)"/>
    <polygon points="0,876 615,737 615,1349 0,1497" fill="var(--blush)"/>
  </svg>

  <div class="brand-mark"></div>
  <div class="line brand-name">ATELIER Z</div>
  <div class="line brand-sub">SCHOONHEIDSINSTITUUT</div>

  <div class="line studio-name">LINEA</div>
  <div class="line studio-by">PERMANENT MAKE UP BY LOTTE VERHAEGEN</div>

  <div class="line dept dept--beauty">SCHOONHEIDSINSTITUUT</div>
  <div class="line detail detail--web1">www.atelierz-demo.be</div>
  <div class="line detail detail--book">enkel op afspraak, boek online</div>
  <div class="line dept dept--pmu">PERMANENT MAKE UP</div>
  <div class="line detail detail--web2">www.linea-demo.be</div>
  <div class="line detail detail--advice">gratis advies enkel op afspraak</div>
  <div class="line detail detail--phone">04 86 51 93 40</div>

  <div class="socials socials--atelier">
    <span class="social"></span><span class="social"></span><span class="social"></span>
  </div>
</section>

<section class="billboard billboard--kernhuis" aria-label="Billboard Kernhuis Marvelde">
  <svg class="billboard__shapes" viewBox="0 0 615 1674" preserveAspectRatio="none" aria-hidden="true">
    <polygon points="0,456 192,491 0,535" fill="var(--shade)"/>
    <polygon points="412,889 615,840 615,927" fill="var(--shade)"/>
    <polygon points="0,535 615,396 615,840 0,988" fill="var(--green)"/>
  </svg>

  <div class="k-name">KERNHUIS<br>MARVELDE</div>

  <div class="line tagline">UW RUG IS ONZE ZORG</div>
  <div class="line k-detail k-web">www.kernhuismarvelde-demo.be</div>
  <div class="line k-detail k-phone">094812670</div>
  <div class="line k-detail k-mail">hello@kernhuismarvelde-demo.be</div>

  <div class="socials socials--kernhuis">
    <span class="social"></span><span class="social"></span>
  </div>
</section>

</body>
</html>
```